Re-design of Business Card

We require a design for our business card.

Korrim is a supplier of industrial packaging specializing in plastic products. We are undergoing a rebranding to appear more corporate. We have changed our company name to korrim and have a new logo.

I have uploaded our old card design with the previous company name.
Don't copy the current design. We are looking for a new design.

Industry/Entity Type

Manufacturing

Contact Information for Business Card

please don't copy the current design. we are looking for a new design.

Font styles to use
Sans Serif

Colors

Designer to choose colors to be used in the design.

Requirements
Must have
• clean and easy to read.

```html
<!DOCTYPE html>
<html lang="en">
<head>
<meta charset="utf-8">
<title>Korrim Business Card</title>
<link rel="stylesheet" href="https://fonts.googleapis.com/css2?family=Jost:wght@400;500;700&display=swap">
<style>
  :root {
    --card-yellow: #f6bc2a;
    --ink: #111111;
    --white: #ffffff;
    --logo-gold: #9a7414;
    --map-tan: #bf9a52;
    --badge-dark: #1a1a1a;
    --page: #ffffff;
  }
  * { margin: 0; padding: 0; box-sizing: border-box; }
  html, body {
    width: 1200px; height: 790px; overflow: hidden;
    background: var(--page);
    font-family: "Jost", Arial, sans-serif;
    color: var(--ink);
  }
  .canvas { position: relative; width: 1200px; height: 790px; }
  .card {
    position: absolute; width: 520px; height: 312px;
    background: var(--card-yellow);
  }
  .card--front { left: 101px; top: 77px; }
  .card--back { left: 560px; top: 359px; }
  .abs { position: absolute; white-space: nowrap; line-height: 1; }

  .site-url { left: 50px; top: 34px; font-size: 12px; font-weight: 700; color: var(--white); letter-spacing: 0.3px; }
  .brand-name { left: 262px; top: 66px; font-size: 52px; font-weight: 700; color: var(--logo-gold); letter-spacing: 1px; }

  .person { left: 50px; top: 206px; }
  .person__name { font-size: 20px; font-weight: 400; line-height: 22px; }
  .person__role { font-size: 12.5px; line-height: 16px; letter-spacing: 0.4px; }
  .person__phone { font-size: 15.5px; line-height: 17px; }
  .person__email { font-size: 12.5px; line-height: 16px; letter-spacing: 0.6px; }

  .office { left: 234px; top: 209px; font-size: 12.5px; letter-spacing: -0.3px; }
  .office__line { display: flex; align-items: center; gap: 4px; height: 16px; }
  .office__dot { width: 9px; height: 9px; border-radius: 50%; background: var(--ink); display: inline-block; }
  .office__gap { width: 14px; }

  .badge {
    position: absolute; left: 47px; width: 66px; height: 66px;
    border: 4px solid var(--badge-dark); border-radius: 50%;
  }
  .badge--one { top: 43px; }
  .badge--two { top: 124px; }
  .badge--three { top: 206px; }

  .services { position: absolute; left: 140px; top: 29px; }
  .services__group { list-style: none; margin-bottom: 13px; }
  .services__group--indent { padding-left: 2px; }
  .services__item { position: relative; padding-left: 8px; font-size: 11.5px; line-height: 14px; letter-spacing: 0.3px; }
  .services__item::before { content: ""; position: absolute; left: 0; top: 6px; width: 2px; height: 2px; border-radius: 50%; background: var(--white); }
  .services__heading { font-weight: 700; color: var(--white); font-size: 12px; }
  .services__wrap { padding-left: 8px; font-size: 11.5px; line-height: 14px; letter-spacing: 0.3px; }

  .coverage-map { position: absolute; left: 326px; top: 164px; width: 168px; height: 132px; border-radius: 40% 45% 35% 30%; background: var(--map-tan); }
</style>
</head>
<body>
<div class="canvas">
  <section class="card card--front">
    <div class="abs site-url">WWW.KORRIM.COM.AU</div>
    <div class="abs brand-name">KORRIM</div>

    <div class="abs person">
      <div class="person__name">DanaWhitlock</div>
      <div class="person__role">Machinery Sale Manager</div>
      <div class="person__phone">000 000 00</div>
      <div class="person__email">dana@korrim.com.au</div>
    </div>

    <div class="abs office">
      <div class="office__line">Head Office:</div>
      <div class="office__line"><span class="office__dot"></span>48 Harlow St. Eastgate Park, Qld 4120 AUS.</div>
      <div class="office__line"><span class="office__dot"></span>1300 555 014<span class="office__gap"></span><span class="office__dot"></span>+617 3000 4521</div>
      <div class="office__line"><span class="office__dot"></span>www.harlowpack.com.au</div>
    </div>
  </section>

  <section class="card card--back">
    <div class="badge badge--one" role="img" aria-label="Quality certification badge"></div>
    <div class="badge badge--two" role="img" aria-label="Food safety certification badge"></div>
    <div class="badge badge--three" role="img" aria-label="Distribution coverage badge"></div>

    <div class="services">
      <ul class="services__group">
        <li class="services__item services__heading">FLEXIBLE PACKAGING</li>
        <li class="services__item">Carton Liners</li>
        <li class="services__item">Tube</li>
        <li class="services__item">Film &amp; Sheet</li>
        <li class="services__item">Printed films(12 col)</li>
        <li class="services__item">Shrink films</li>
      </ul>
      <ul class="services__group">
        <li class="services__item services__heading">PALLET WRAPPING MACHINERY</li>
        <li class="services__item">Semi &amp; Fully Auto lines</li>
        <li class="services__item">Finance options include Lease,</li>
        <li class="services__wrap">Rent, pay per wrap</li>
      </ul>
      <ul class="services__group services__group--indent">
        <li class="services__item services__heading">PALLET CONTAINMENT</li>
        <li class="services__item">Stretch</li>
        <li class="services__item">Heat Shrink</li>
        <li class="services__item">Pallet Hood</li>
      </ul>
      <ul class="services__group services__group--indent">
        <li class="services__item services__heading">GENERAL PACKAGING</li>
      </ul>
    </div>

    <div class="coverage-map" role="img" aria-label="Map of Australia and New Zealand marking distribution locations"></div>
  </section>
</div>
</body>
</html>
```